Labels for an activated Charcoal Facial Wash, Scrub and Mask

We need a new label design for a new line of Facial products. The product, falls under our Brand Dovelin and is based on Activated Charcoal. Activated Black Charcoal Facial wash (250ml), Activated Black Charcoal Mask (100gms) and Activated Black Charcoal face scrub (100gms). We would like to see designs that are modern, clean and must communicate natural products.

```html
<!DOCTYPE html>
<html lang="en">
<head>
<meta charset="UTF-8">
<title>Dovelin – Activated Black Charcoal Facial Wash Label</title>
<link href="https://fonts.googleapis.com/css2?family=Cinzel:wght@400&family=Raleway:wght@300;400;500&family=Cutive+Mono&display=swap" rel="stylesheet">
<style>
  :root {
    --canvas-bg: #f4f2ee;
    --label-black: #0e0e0e;
    --label-edge: #1c1c1c;
    --gold: #b8954f;
    --gold-light: #d6b673;
    --white: #f5f5f2;
    --muted: #cfcfca;
    --leaf-tone: rgba(184, 149, 79, 0.14);
  }
  * { margin: 0; padding: 0; box-sizing: border-box; }
  html, body {
    width: 1200px;
    height: 1037px;
    overflow: hidden;
    background: var(--canvas-bg);
  }
  .canvas {
    width: 1200px;
    height: 1037px;
    display: flex;
    align-items: center;
    justify-content: center;
  }
  .label {
    position: relative;
    width: 440px;
    height: 960px;
    background: linear-gradient(90deg, var(--label-edge) 0%, var(--label-black) 18%, var(--label-black) 82%, var(--label-edge) 100%);
    color: var(--white);
    overflow: hidden;
  }
  .brand {
    position: absolute;
    top: 238px;
    left: 0;
    right: 0;
    display: flex;
    align-items: center;
    justify-content: center;
    gap: 14px;
  }
  .brand-mark {
    width: 12px;
    height: 12px;
    border: 1px solid var(--gold);
  }
  .brand-name {
    font-family: "Cinzel", serif;
    font-weight: 400;
    font-size: 26px;
    letter-spacing: 9px;
    color: var(--gold);
  }
  .product-title {
    position: absolute;
    top: 410px;
    left: 0;
    right: 0;
    text-align: center;
    font-family: "Raleway", sans-serif;
    line-height: 1.12;
  }
  .product-title .line {
    display: block;
    font-size: 40px;
    letter-spacing: 1px;
  }
  .product-title .line--light {
    font-weight: 300;
    color: var(--white);
  }
  .product-title .line--accent {
    font-weight: 500;
    color: var(--gold-light);
  }
  .divider {
    position: absolute;
    top: 582px;
    left: 50%;
    width: 44px;
    height: 3px;
    margin-left: -22px;
    background: var(--white);
  }
  .claims {
    position: absolute;
    top: 604px;
    left: 0;
    right: 0;
    text-align: center;
    font-family: "Cutive Mono", monospace;
    font-size: 15px;
    letter-spacing: 0.5px;
    line-height: 1.65;
    color: var(--muted);
  }
  .leaf-decoration {
    position: absolute;
    left: 18px;
    top: 640px;
    width: 230px;
    height: 300px;
    border-radius: 50% 50% 50% 10%;
    background: radial-gradient(ellipse at 40% 45%, var(--leaf-tone) 0%, rgba(184,149,79,0.05) 60%, transparent 80%);
  }
  .volume {
    position: absolute;
    top: 830px;
    left: 0;
    right: 0;
    text-align: center;
    font-family: "Raleway", sans-serif;
    font-weight: 400;
    font-size: 18px;
    color: var(--white);
  }
</style>
</head>
<body>
<main class="canvas">
  <section class="label">
    <div class="brand">
      <span class="brand-mark"></span>
      <span class="brand-name">DOVELIN</span>
    </div>

    <h1 class="product-title">
      <span class="line line--light">ACTIVATED</span>
      <span class="line line--accent">BLACK CHARCOAL</span>
      <span class="line line--light">FACIAL WASH</span>
    </h1>

    <div class="divider"></div>

    <p class="claims">PROTECT AND PROMOTE CLEAR SKIN<br>OIL CONTROL</p>

    <div class="leaf-decoration" role="img" aria-label="Faint gold line drawing of a leafy botanical sprig"></div>

    <p class="volume">7 fl oz. ( 250ml )</p>
  </section>
</main>
</body>
</html>
```